Small rum distillery looking for bottle design

Small rum distillery in Estonia. Looking for bottle lable design. It should be simple but at the same time point out from the variety of other bottles.
As we are a small nordic country, design can be some how nordic or represent our country. It can also have some connection with sailing or sea as we know it pirates love it.
Bottle we are using is Brisela 500

Industry/Entity Type

food and beverage

Other font styles liked:
• Baskerville

```html
<!DOCTYPE html>
<html lang="en">
<head>
<meta charset="utf-8">
<title>Halvik Distillery – Estonian Rum Label</title>
<link rel="stylesheet" href="https://fonts.googleapis.com/css2?family=Libre+Baskerville:wght@400;700&display=swap">
<style>
  :root {
    --page: #ffffff;
    --label-dark: #3d3d40;
    --cream: #f4f2ea;
    --rum-red: #c0282d;
    --ink: #3d3d40;
  }
  html, body {
    margin: 0;
    padding: 0;
    width: 1200px;
    height: 1200px;
    overflow: hidden;
    background: var(--page);
  }
  .canvas {
    position: relative;
    width: 1200px;
    height: 1200px;
  }
  .label {
    position: absolute;
    left: 71px;
    top: 108px;
    width: 1058px;
    height: 983px;
  }
  .label-body { fill: var(--label-dark); }
  .label-rule { fill: none; stroke: var(--cream); stroke-width: 4; }
  .brand-name {
    font-family: "Libre Baskerville", Baskerville, serif;
    font-size: 42px;
    fill: var(--cream);
    letter-spacing: 1px;
  }
  .brand-sub {
    font-family: "Libre Baskerville", Baskerville, serif;
    font-size: 12px;
    fill: var(--cream);
    letter-spacing: 6px;
  }
  .brand-dot { fill: none; stroke: var(--cream); stroke-width: 2; }
  .map-area { fill: var(--cream); }
  .origin {
    font-family: "Libre Baskerville", Baskerville, serif;
    font-size: 34px;
    fill: var(--ink);
  }
  .spirit {
    font-family: "Libre Baskerville", Baskerville, serif;
    font-weight: 700;
    font-size: 100px;
    fill: var(--rum-red);
  }
  .spec {
    font-family: "Libre Baskerville", Baskerville, serif;
    font-size: 20px;
    fill: var(--cream);
  }
</style>
</head>
<body>
<div class="canvas">
  <svg class="label" viewBox="90 153 705 655" xmlns="http://www.w3.org/2000/svg">
    <rect class="label-body" x="90" y="335" width="705" height="405"/>
    <path class="label-body" d="M215 808 V380 A227 227 0 0 1 669 380 V808 Z"/>

    <polyline class="label-rule" points="218,353 108,353 108,720 218,720"/>
    <polyline class="label-rule" points="667,353 777,353 777,720 667,720"/>
    <path class="label-rule" d="M237 785 V380 A205 205 0 0 1 647 380 V785 Z"/>

    <circle class="brand-dot" cx="442" cy="262" r="11"/>
    <text class="brand-name" x="442" y="340" text-anchor="middle">HALVIK</text>
    <line class="label-rule" x1="345" y1="350" x2="537" y2="350" stroke-width="2"/>
    <text class="brand-sub" x="442" y="371" text-anchor="middle">DISTILLERY</text>

    <rect class="map-area" x="252" y="438" width="384" height="245" rx="24"
          role="img" aria-label="Silhouette map of Estonia"/>
    <text class="origin" x="400" y="507">Estonian</text>
    <text class="spirit" x="290" y="575">Rum</text>

    <text class="spec" x="268" y="757">40%</text>
    <text class="spec" x="620" y="757" text-anchor="end">700ml</text>
  </svg>
</div>
</body>
</html>
```